Artist needs a business card for her pencil portraits and streetscapes

My mum is an artist and does fabulous portraits and sketches with pencil and needs a business card.
She likes designs that are a bit weird or unusual. The winning design will NOT be a slick modern corporate looking logo. It should be a little bit rustic and different. Interesting patterns and textures would be great, it doesn't even need to look like a business card! Come up with something unique!

Target Market(s)

Older clientele looking for family portraits

Industry/Entity Type

Artists

Contact Information for Business Card

Basically just need the name and contact details

Font styles to use
Decorative
Script

Requirements
Must have
• Lena Dorsby
• Artist
• 0427193662
• lenadorsby@postvale.com
Nice to have
• Weird artistic backgrounds, interesting textures, unusual designs for an artistic woman.
Should not have
• Nothing ultra modern and nothing corporate looking.

```html
<!DOCTYPE html>
<html lang="en">
<head>
<meta charset="utf-8">
<title>Lena Dorsby · Artist</title>
<link rel="stylesheet" href="https://fonts.googleapis.com/css2?family=Courgette&family=Carlito&family=Open+Sans:wght@400&display=swap">
<style>
  :root {
    --paper: #e7e9e7;
    --paper-light: #f1f2f0;
    --paper-shade: #dadddb;
    --ink: #484848;
    --sketch-light: #e2e5e3;
    --sketch-mid: #c8cecb;
    --sketch-dark: #a3aba8;
  }
  html, body {
    margin: 0;
    padding: 0;
    overflow: hidden;
    background: var(--paper);
  }
  .card {
    position: relative;
    width: 1200px;
    height: 680px;
    overflow: hidden;
    background:
      radial-gradient(circle at 25% 30%, var(--paper-light) 0, transparent 45%),
      radial-gradient(circle at 80% 75%, var(--paper-shade) 0, transparent 55%),
      var(--paper);
  }
  .card__paper-grain {
    position: absolute;
    inset: 0;
    width: 100%;
    height: 100%;
    mix-blend-mode: multiply;
  }
  .card__illustration {
    position: absolute;
    left: 124px;
    top: 28px;
    width: 338px;
    height: 640px;
    background:
      radial-gradient(ellipse at 50% 18%, var(--sketch-mid) 0, transparent 60%),
      linear-gradient(180deg, var(--sketch-light) 0%, var(--sketch-mid) 60%, var(--sketch-dark) 100%);
    border-radius: 8px;
    opacity: 0.8;
  }
  .card__name {
    position: absolute;
    left: 472px;
    top: 322px;
    margin: 0;
    font-family: "Courgette", cursive;
    font-weight: 400;
    font-size: 100px;
    line-height: 1;
    color: var(--ink);
    white-space: nowrap;
  }
  .card__role {
    position: absolute;
    right: 156px;
    top: 442px;
    margin: 0;
    font-family: "Carlito", sans-serif;
    font-size: 80px;
    line-height: 1;
    color: var(--ink);
  }
  .card__contact {
    position: absolute;
    right: 114px;
    top: 542px;
    margin: 0;
    text-align: right;
    font-family: "Open Sans", sans-serif;
    font-size: 33px;
    line-height: 50px;
    letter-spacing: 2.5px;
    color: var(--ink);
  }
  .card__contact-line {
    display: block;
    white-space: nowrap;
  }
</style>
</head>
<body>
  <main class="card">
    <svg class="card__paper-grain" viewBox="0 0 1200 680" aria-hidden="true">
      <defs>
        <filter id="paper-grain" x="0" y="0" width="100%" height="100%">
          <feTurbulence type="fractalNoise" baseFrequency="0.32 0.75" numOctaves="3" seed="7" result="noise"/>
          <feDiffuseLighting in="noise" surfaceScale="2.4" lighting-color="#f4f5f3" result="lit">
            <feDistantLight azimuth="55" elevation="58"/>
          </feDiffuseLighting>
        </filter>
      </defs>
      <rect width="1200" height="680" filter="url(#paper-grain)"/>
    </svg>

    <div class="card__illustration" role="img" aria-label="Pencil sketch of poppies on long stems in a small patterned porcelain vase"></div>

    <h1 class="card__name">Lena Dorsby</h1>
    <p class="card__role">artist</p>
    <p class="card__contact">
      <span class="card__contact-line">phone:0427193662</span>
      <span class="card__contact-line">lenadorsby@postvale.com</span>
    </p>
  </main>
</body>
</html>
```